Brochure Design*

We are seeking a simple but powerful brochure design for our new company that uses electrostatic sprayers for the treatment and prevention of Covid 19 for businesses throughout the Southeast. The current brochure has too many photos and very distracting, i personally do not like anything about the brochure. Our sister company Harlow Print Supply was founded in 1983. Our company HPS Services LLC website is www.hpsvx.com
Updates

We need a few more days to receive feedback from our employees. Thank You

Target Market(s)

Business owners

Font styles to use
Serif
Sans Serif

Requirements
Must have
• A call for action brochure, simple while delivering a strong message
Should not have
• CLUTTER,

```html
<!DOCTYPE html>
<html lang="en">
<head>
<meta charset="utf-8">
<title>HPS Services LLC – Electrostatic Disinfecting Brochure</title>
<link href="https://fonts.googleapis.com/css2?family=Roboto:wght@400;500;700&family=Titillium+Web:wght@400;600&family=Archivo+Black&display=swap" rel="stylesheet">
<style>
  :root {
    --green: #33b240;
    --green-deep: #2a9a37;
    --green-bright: #4fe866;
    --charcoal: #262626;
    --charcoal-soft: #3c3c3c;
    --white: #ffffff;
    --grey-logo: #777777;
    --paper: #ffffff;
  }
  * { margin: 0; padding: 0; box-sizing: border-box; }
  html, body { width: 848px; height: 1200px; overflow: hidden; background: var(--paper); }
  .brochure {
    position: relative;
    width: 848px;
    height: 1200px;
    overflow: hidden;
    font-family: "Roboto", Arial, sans-serif;
    color: var(--white);
  }
  .backdrop { position: absolute; inset: 0; }

  .headline {
    position: absolute;
    left: 41px;
    font-family: "Roboto", Arial, sans-serif;
    font-weight: 700;
    font-size: 29px;
    line-height: 35px;
    letter-spacing: 0.1px;
    text-transform: uppercase;
  }
  .headline--intro { top: 54px; }
  .headline--germs { top: 404px; }

  .copy {
    position: absolute;
    left: 42px;
    font-size: 14px;
    line-height: 17px;
    letter-spacing: 0.1px;
  }
  .copy--intro { top: 167px; }
  .copy--germs { top: 486px; }
  .copy .ln {
    display: block;
    white-space: nowrap;
    text-align: justify;
    text-align-last: justify;
    margin-left: var(--l, 0px);
    width: var(--w);
  }
  .copy .ln--end { text-align-last: left; }

  .logo {
    position: absolute;
    left: 548px;
    top: 42px;
    width: 252px;
    text-align: center;
    font-family: "Archivo Black", Arial, sans-serif;
    font-weight: 400;
    color: var(--green-bright);
    line-height: 1;
  }
  .logo__name { display: block; font-size: 58px; letter-spacing: 6px; }
  .logo__suffix { display: block; font-size: 24px; letter-spacing: 2px; margin-top: 6px; }

  .product-visual {
    position: absolute;
    left: 448px;
    top: 188px;
    width: 392px;
    height: 398px;
    border-radius: 40px;
    background: radial-gradient(ellipse at 40% 45%, #d9dbe0 0%, #9a9ca3 45%, rgba(60,60,66,0.55) 75%, rgba(255,255,255,0) 100%);
  }

  .services {
    position: absolute;
    left: 467px;
    top: 672px;
  }
  .services__title {
    font-family: "Roboto", Arial, sans-serif;
    font-weight: 700;
    font-size: 31px;
    line-height: 40px;
    margin-bottom: 10px;
  }
  .services__list { list-style: none; }
  .services__item {
    display: flex;
    align-items: center;
    font-family: "Titillium Web", Arial, sans-serif;
    font-size: 24px;
    line-height: 38px;
    height: 38px;
  }
  .services__item svg { width: 12px; height: 14px; margin-right: 8px; flex: none; }

  .virus-visual {
    position: absolute;
    right: -40px;
    bottom: -60px;
    width: 440px;
    height: 300px;
    background:
      radial-gradient(circle at 20% 22%, rgba(90,230,110,0.95) 0 28px, rgba(90,230,110,0) 52px),
      radial-gradient(circle at 62% 62%, rgba(110,240,130,0.7) 0 90px, rgba(110,240,130,0) 170px);
  }

  .contact {
    position: absolute;
    left: 44px;
    top: 1036px;
  }
  .contact__row { display: flex; align-items: center; }
  .contact__row svg { flex: none; }
  .contact__phone {
    font-family: "Roboto", Arial, sans-serif;
    font-weight: 700;
    font-size: 36px;
    line-height: 48px;
    margin-left: 8px;
  }
  .contact__text {
    font-family: "Roboto", Arial, sans-serif;
    font-weight: 500;
    font-size: 23px;
    line-height: 30px;
    margin-left: 14px;
  }
  .contact__row--email { margin-top: 11px; }
  .contact__row--address { margin-top: 11px; }
</style>
</head>
<body>
<main class="brochure">

  <svg class="backdrop" width="848" height="1200" viewBox="0 0 848 1200" aria-hidden="true">
    <defs>
      <linearGradient id="greenField" x1="0" y1="0" x2="1" y2="0">
        <stop offset="0" stop-color="#2c9d39"/>
        <stop offset="0.5" stop-color="#33b240"/>
      </linearGradient>
      <linearGradient id="darkBase" x1="0" y1="0" x2="0" y2="1">
        <stop offset="0" stop-color="#262626"/>
        <stop offset="1" stop-color="#3a3a3a"/>
      </linearGradient>
    </defs>
    <rect width="848" height="1200" fill="var(--paper)"/>
    <ellipse class="services-disc" cx="692" cy="882" rx="317" ry="297" fill="var(--charcoal)"/>
    <path class="green-field" d="M0,0 H470 C516,90 520,240 440,340 C385,410 305,480 300,640 C296,800 380,960 470,1050 L0,1050 Z" fill="url(#greenField)"/>
    <path class="dark-sweep" d="M0,760 C120,860 260,985 470,1050 C600,1060 760,1058 848,1050 V1200 H0 Z" fill="url(#darkBase)"/>
  </svg>

  <h1 class="headline headline--intro">High quality environmental<br>cleaning and disinfecting<br>of surfaces</h1>

  <p class="copy copy--intro">
    <span class="ln" style="--w:413px">In light of coronavirus (SARS-CoV-2), environmental cleaning and</span>
    <span class="ln" style="--w:413px">disinfecting of surfaces have become more important than ever</span>
    <span class="ln" style="--w:413px">before. Research studies show that environmental cleaning and</span>
    <span class="ln" style="--w:410px">disinfection play important roles in helping to prevent the spread</span>
    <span class="ln" style="--w:407px">of infection. New technology in this industry is the application of</span>
    <span class="ln" style="--w:403px">EPA-approved disinfectants utilizing electrostatic application</span>
    <span class="ln" style="--w:398px">systems for proper surface disinfection. Electrostatics is a</span>
    <span class="ln" style="--w:391px">proven technology in the agricultural and automotive indus-</span>
    <span class="ln" style="--w:382px">tries. This technology is now being integrated into the infec-</span>
    <span class="ln" style="--w:371px">tion prevention and control industry as a tool to break the</span>
    <span class="ln ln--end" style="--w:371px">chain of pathogen mobility.</span>
  </p>

  <div class="logo">
    <span class="logo__name">HPS</span>
    <span class="logo__suffix">SERVICES, LLC</span>
  </div>

  <div class="product-visual" role="img" aria-label="Handheld electrostatic disinfectant sprayer with battery pack and backpack sprayer unit"></div>

  <h2 class="headline headline--germs">How long do germs<br>stay on surfaces?</h2>

  <p class="copy copy--germs">
    <span class="ln" style="--w:270px">SARS-CoV-2 can remain on surfaces for</span>
    <span class="ln" style="--w:262px">hours and up to 9 days. Research has</span>
    <span class="ln" style="--w:256px">shown that microorganisms can survive</span>
    <span class="ln" style="--w:250px">on surfaces for days, weeks, and even</span>
    <span class="ln" style="--w:245px">months, and can be hidden from cur-</span>
    <span class="ln" style="--w:240px">rent spray and wipe methods. (Kel-</span>
    <span class="ln" style="--w:236px">ler, 2006) Using electrostatic technol-</span>
    <span class="ln" style="--w:234px">ogy provides effective, proven, safe</span>
    <span class="ln" style="--w:232px">and comprehensive surface cover-</span>
    <span class="ln" style="--w:230px">age and eliminates cross-contami-</span>
    <span class="ln ln--end" style="--w:230px">nation of dangerous pathogens.</span>
    <span class="ln" style="--w:229px">Most surface areas are neutral</span>
    <span class="ln ln--end" style="--w:229px">(uncharged) or negative.</span>
    <span class="ln" style="--w:230px">Electrostatic application for surface</span>
    <span class="ln" style="--w:231px">disinfection is a method of applying</span>
    <span class="ln" style="--w:233px">EPA-registered disinfectants to a</span>
    <span class="ln" style="--l:2px;--w:233px">target surface area by utilizing the</span>
    <span class="ln" style="--l:12px;--w:227px">electrostatic force of attraction.</span>
    <span class="ln" style="--l:22px;--w:221px">Simply put, the electrostatic</span>
    <span class="ln" style="--l:34px;--w:214px">system places an electrical</span>
    <span class="ln" style="--l:48px;--w:205px">charge on the droplets and dis-</span>
    <span class="ln" style="--l:62px;--w:197px">perses them across a target</span>
    <span class="ln" style="--l:79px;--w:183px">surface area, providing a</span>
    <span class="ln" style="--l:100px;--w:175px">comprehensive, even cover-</span>
    <span class="ln ln--end" style="--l:126px;--w:100px">age.</span>
  </p>

  <section class="services">
    <h2 class="services__title">OUR SERVICES</h2>
    <ul class="services__list">
      <li class="services__item"><svg viewBox="0 0 12 14"><path d="M1 0 L12 7 L1 14 L4 7 Z" fill="var(--green-bright)"/></svg>Offices Banks</li>
      <li class="services__item"><svg viewBox="0 0 12 14"><path d="M1 0 L12 7 L1 14 L4 7 Z" fill="var(--green-bright)"/></svg>Bars Restaurants</li>
      <li class="services__item"><svg viewBox="0 0 12 14"><path d="M1 0 L12 7 L1 14 L4 7 Z" fill="var(--green-bright)"/></svg>Gyms Sports Facilities</li>
      <li class="services__item"><svg viewBox="0 0 12 14"><path d="M1 0 L12 7 L1 14 L4 7 Z" fill="var(--green-bright)"/></svg>Medical Hospitals</li>
      <li class="services__item"><svg viewBox="0 0 12 14"><path d="M1 0 L12 7 L1 14 L4 7 Z" fill="var(--green-bright)"/></svg>Schools Daycares</li>
      <li class="services__item"><svg viewBox="0 0 12 14"><path d="M1 0 L12 7 L1 14 L4 7 Z" fill="var(--green-bright)"/></svg>Data Centers 911 Call Centers</li>
    </ul>
  </section>

  <div class="virus-visual" role="img" aria-label="Soft green illustration of virus particles"></div>

  <address class="contact" style="font-style:normal">
    <div class="contact__row contact__row--phone">
      <svg width="24" height="24" viewBox="0 0 24 24" aria-hidden="true">
        <circle cx="12" cy="12" r="10.5" fill="none" stroke="var(--white)" stroke-width="2"/>
        <path d="M8.2 6.5 L10 8.8 L9 10.4 C9.8 12 11.9 14.2 13.6 15 L15.2 14 L17.5 15.8 L16.3 17.6 C12.5 17.8 6.4 11.8 6.4 7.7 Z" fill="var(--white)"/>
      </svg>
      <span class="contact__phone">888-402-7751</span>
    </div>
    <div class="contact__row contact__row--email">
      <svg width="18" height="14" viewBox="0 0 18 14" aria-hidden="true">
        <rect x="1" y="1" width="16" height="12" fill="none" stroke="var(--white)" stroke-width="1.5"/>
        <path d="M1 1 L9 8 L17 1" fill="none" stroke="var(--white)" stroke-width="1.5"/>
      </svg>
      <span class="contact__text">info@hpsvx.com</span>
    </div>
    <div class="contact__row contact__row--address">
      <svg width="18" height="22" viewBox="0 0 18 22" aria-hidden="true">
        <path d="M9 1 C4.6 1 1.5 4.3 1.5 8.4 C1.5 13.5 9 21 9 21 C9 21 16.5 13.5 16.5 8.4 C16.5 4.3 13.4 1 9 1 Z" fill="none" stroke="var(--white)" stroke-width="1.5"/>
        <circle cx="9" cy="8.4" r="2.6" fill="none" stroke="var(--white)" stroke-width="1.5"/>
      </svg>
      <span class="contact__text">150 Oak Ridge Plaza Raleigh, NC 27615</span>
    </div>
  </address>

</main>
</body>
</html>
```